Email Signature Design

Please design an email signature, the below is an example of our current design;
___

CARRODY ESTATE HOLDINGS PTY LTD
BENEDICT HARLOWE
Licensed Strata and Community Manager

143 Tallowood Street,
KELDARRA NSW 2093

P: 02.9473.6820 F: 9536.2048
Website: www.carrodyestate.com.au

This e-mail message and accompanying data may contain information that is confidential and private. If you are not the intended recipient, the use, dissemination, distribution or copying of this message or data is prohibited.

If you have received this e-mail in error please notify us immediately and delete all material pertaining to this e-mail. strata@carrodyestate.com.au

___

We would like to incorporate our logo and company colours, you can view the colours and feel of image at www.carrodyestate.com.au

Industry/Entity Type

It Company

Requirements
Must have
• use of logo and company colours (image)

```html
<!DOCTYPE html>
<html lang="en">
<head>
<meta charset="utf-8">
<title>Carrody Estate Group – Email Signature</title>
<link rel="stylesheet" href="https://fonts.googleapis.com/css2?family=Source+Sans+3:wght@400;600;700&display=swap">
<style>
  :root {
    --page-bg: #e9e7e3;
    --card-bg: #ffffff;
    --band-grey: #6d6e70;
    --accent-tan: #e3d2ab;
    --brand-olive: #7f7a3b;
    --text-dark: #4a4a4a;
    --text-mid: #6d6e70;
    --icon-grey: #666666;
    --divider: #d6d6d6;
  }
  * { margin: 0; padding: 0; box-sizing: border-box; }
  html, body {
    width: 1200px; height: 442px; overflow: hidden;
    background: var(--page-bg);
    font-family: "Source Sans 3", sans-serif;
  }
  .signature {
    position: absolute; left: 43px; top: 27px;
    width: 1121px; height: 373px;
    background: var(--card-bg);
    box-shadow: 0 1px 3px rgba(0,0,0,.25);
    overflow: hidden;
  }
  .header-band {
    position: absolute; left: 0; top: 0; width: 100%; height: 113px;
    background: var(--band-grey);
  }
  .accent-rule {
    position: absolute; left: 0; top: 118px; width: 100%; height: 3px;
    background: var(--accent-tan);
  }
  .brand-mark {
    position: absolute; left: 418px; top: 22px;
    width: 124px; height: 124px;
    background: var(--brand-olive);
    border: 6px solid var(--card-bg);
  }
  .brand-name {
    position: absolute; left: 404px; top: 171px;
    font-size: 26px; font-weight: 700; letter-spacing: .3px;
    color: var(--brand-olive); line-height: 1;
  }
  .brand-tagline {
    position: absolute; left: 404px; top: 199px;
    font-size: 18px; font-weight: 400; letter-spacing: .6px;
    color: var(--text-mid); line-height: 1;
  }
  .person {
    position: absolute; right: 567px; top: 253px;
    text-align: right; color: var(--text-dark);
    font-size: 20px; line-height: 24px;
  }
  .person-name { color: var(--brand-olive); font-weight: 700; font-size: 21px; }
  .person-role { margin-bottom: 5px; }
  .company-name { color: var(--text-mid); }
  .divider {
    position: absolute; left: 573px; top: 250px;
    width: 1px; height: 105px; background: var(--divider);
  }
  .contacts {
    position: absolute; left: 597px; top: 253px;
    list-style: none; color: var(--text-dark);
    font-size: 20px; line-height: 27px;
  }
  .contacts li { display: flex; align-items: center; }
  .contact-icon {
    width: 16px; height: 16px; margin-right: 13px;
    fill: none; stroke: var(--icon-grey); stroke-width: 1.5;
  }
  .contact-icon .solid { fill: var(--icon-grey); stroke: none; }
</style>
</head>
<body>
  <div class="signature">
    <div class="header-band"></div>
    <div class="accent-rule"></div>
    <div class="brand-mark"></div>
    <div class="brand-name">CARRODY ESTATE GROUP</div>
    <div class="brand-tagline">STRATA MANAGEMENT SERVICES</div>

    <div class="person">
      <div class="person-name">BENEDICT HARLOWE</div>
      <div class="person-role">Licensed Strata and Community Manager</div>
      <div class="company-name">CARRODY ESTATE HOLDINGS PTY LTD</div>
      <div class="address">143 Tallowood Street, KELDARRA NSW 2093</div>
    </div>

    <div class="divider"></div>

    <ul class="contacts">
      <li>
        <svg class="contact-icon" viewBox="0 0 16 16" aria-hidden="true">
          <circle cx="8" cy="8" r="7"/>
          <path class="solid" d="M5.5 4.2l1.4-.3.7 1.8-.9.7c.4 1 1.1 1.8 2 2.3l.8-.8 1.7.8-.3 1.4c-2.8.2-5.6-2.9-5.4-5.9z"/>
        </svg>
        02.9473.6820
      </li>
      <li>
        <svg class="contact-icon" viewBox="0 0 16 16" aria-hidden="true">
          <path class="solid" d="M4 2h6l2 2v3H4z"/>
          <path class="solid" d="M1 8h14v6H1z"/>
          <rect x="4" y="10" width="8" height="2" fill="#fff" stroke="none"/>
        </svg>
        9536.2048
      </li>
      <li>
        <svg class="contact-icon" viewBox="0 0 16 16" aria-hidden="true">
          <path class="solid" d="M1 4h14v9H1z"/>
          <path d="M1.5 4.5L8 9l6.5-4.5" stroke="#fff"/>
        </svg>
        strata@carrodyestate.com.au
      </li>
      <li>
        <svg class="contact-icon" viewBox="0 0 16 16" aria-hidden="true">
          <circle cx="8" cy="8" r="7"/>
          <ellipse cx="8" cy="8" rx="3" ry="7"/>
          <path d="M1 8h14M2.5 4.5h11M2.5 11.5h11"/>
        </svg>
        www.carrodyestate.com.au
      </li>
    </ul>
  </div>
</body>
</html>
```